Professional
Mark Elwood
President
4217 Vista Arroyo Place, NW
Albuquerque, NM 87114
melwood@emibq.com
www.emibq.com
New Construction*Remodels* Renovations*Handyman Services
Here is my logo for the stationary and business cards
Logo .AI file

```html
<!DOCTYPE html>
<html lang="en">
<head>
<meta charset="utf-8">
<title>Elwood Masonry, Inc – Business Card</title>
<link rel="stylesheet" href="https://fonts.googleapis.com/css2?family=Open+Sans:wght@400;600;700;800&display=swap">
<style>
  :root {
    --page-bg: #eceae6;
    --card-red: #e8262d;
    --card-orange: #f7a21b;
    --card-white: #ffffff;
    --ink: #231f20;
    --ink-soft: #3a3a3a;
    --accent-red: #d8232a;
    --divider: #9a9a9a;
  }
  * { margin: 0; padding: 0; box-sizing: border-box; }
  html, body {
    width: 1200px; height: 778px; overflow: hidden;
    background: var(--page-bg);
    font-family: "Open Sans", Arial, sans-serif;
  }
  .canvas { position: relative; width: 1200px; height: 778px; }
  .business-card {
    position: absolute; left: 165px; top: 144px;
    width: 870px; height: 490px;
    border-radius: 26px; overflow: hidden;
    box-shadow: 0 6px 18px rgba(0,0,0,0.18);
  }
  .card-shape { position: absolute; inset: 0; }
  .brand {
    position: absolute; left: 168px; top: 96px;
    display: flex; align-items: center; gap: 22px;
  }
  .brand-mark {
    width: 110px; height: 110px; border-radius: 50%;
    background: var(--card-red); flex: none;
  }
  .brand-name {
    font-weight: 800; font-size: 38px; color: var(--ink);
    letter-spacing: 0.5px; white-space: nowrap;
  }
  .person {
    position: absolute; right: 498px; top: 314px; text-align: right;
  }
  .person-name { color: var(--accent-red); font-size: 25px; font-weight: 600; line-height: 1.3; }
  .person-title { color: var(--ink); font-size: 20px; font-weight: 700; line-height: 1.6; }
  .divider {
    position: absolute; left: 427px; top: 240px;
    width: 1px; height: 228px; background: var(--divider);
  }
  .contact {
    position: absolute; left: 475px; top: 256px;
    font-size: 20px; color: var(--ink-soft); line-height: 31px;
  }
  .contact-list { list-style: none; margin-top: 2px; }
  .contact-item { display: flex; align-items: center; gap: 14px; height: 34px; }
  .contact-icon { width: 20px; height: 20px; flex: none; fill: var(--card-orange); }
</style>
</head>
<body>
<main class="canvas">
  <section class="business-card">
    <svg class="card-shape" viewBox="0 0 870 490" preserveAspectRatio="none" aria-hidden="true">
      <rect width="870" height="490" fill="var(--card-red)"/>
      <path d="M104,0 Q-100,245 104,490 L766,490 Q970,245 766,0 Z" fill="var(--card-orange)"/>
      <path d="M120,0 Q-72,245 120,490 L750,490 Q942,245 750,0 Z" fill="var(--card-white)"/>
    </svg>

    <div class="brand">
      <span class="brand-mark"></span>
      <span class="brand-name">Elwood Masonry, Inc</span>
    </div>

    <div class="person">
      <p class="person-name">Mark Elwood</p>
      <p class="person-title">President</p>
    </div>

    <div class="divider"></div>

    <address class="contact" style="font-style:normal">
      <p>4217 Vista Arroyo Place, NW</p>
      <p>Albuquerque, NM 87114</p>
      <ul class="contact-list">
        <li class="contact-item">
          <svg class="contact-icon" viewBox="0 0 20 20"><path d="M6 1h8a1.5 1.5 0 0 1 1.5 1.5v15A1.5 1.5 0 0 1 14 19H6a1.5 1.5 0 0 1-1.5-1.5v-15A1.5 1.5 0 0 1 6 1zm0 3v11h8V4z"/></svg>
          <span>505-380-2916</span>
        </li>
        <li class="contact-item">
          <svg class="contact-icon" viewBox="0 0 20 20"><path d="M3 8c0-2 2-4 7-4s7 2 7 4v2h-4V8H7v2H3zm1 4h12l1 6H3z"/></svg>
          <span>505-614-0837</span>
        </li>
        <li class="contact-item">
          <svg class="contact-icon" viewBox="0 0 20 20"><path d="M2 4h16v12H2zm2 2v.4l6 4.2 6-4.2V6zm0 2.8V14h12V8.8l-6 4.2z"/></svg>
          <span>melwood@emibq.com</span>
        </li>
        <li class="contact-item">
          <svg class="contact-icon" viewBox="0 0 20 20"><circle cx="10" cy="10" r="8.5"/></svg>
          <span>www.emibq.com</span>
        </li>
      </ul>
    </address>
  </section>
</main>
</body>
</html>
```